Indigenous Mentoring Masterclass

We are a small Indigenous owned company that specializes in mentoring training for anybody who mentors Indigenous mentees: www.tarnlee.com.au

We would like a brochure advertising an upcoming training course being held Parramatta, Sydney, NSW. The brochure should show the course goals and objectives (course syllabus attached)

The brochure to have colouring similar to loggo attached.

The final design should advertise a sharp two day course delivered by specialist Indigenous trainers.
Updates

Hi Everyone,

Hi Res Loggo updated for your use.  Please let me know if you require further help.

Regards

Target Market(s)

Anybody working in the Indigenous Australian domain.

Industry/Entity Type

Advertising

Requirements
Must have
• This new and improved skills - based course has been sharpened to a 2 day program to focus mentors on deep mentoring and therefore creating transformational changes with mentees.

Brochure will have a focus on the trainer capability.

Our Trainers
Under the leadership of TKO’s remarkably accomplished Directors Harriet Dunmore and Gordon Pelkin, the company has gained a reputation across a range of organisations and sectors as a dependable supplier of superior cutting-edge training, facilitation and consultative services, consistently providing the greatest value for money.
The TKO team is made up of highly qualified and practiced individuals with a passion and commitment to providing fresh, innovative and proven approaches to effective training delivery and group facilitation. We are self-motivated and results-focused individuals who achieve proven results for our clients. TKO’s Directors bring together highly competent project teams to achieve proven specific client objectives. These teams can comprise of a number of expert associates in relevant specialist fields, and are linked in to help do so. You will have an opportunity to spend two days with these Directors and ask how you can leverage your mentoring skills within your organization.
TKOs Business lines: agile and scrum, tribal leadership, global diversity and sustainability, culture hacking, leadership, community and organization development, change, coaching and mentoring.

Learning Objectives
After completing the course, you will learn powerful new distinctions that will improve your knowledge and practice base to leverage your mentoring conversations.
Learn practical problem solving and solution focused methods to address mentee concerns and understand and manage moods with yourself, mentees and others.

Learning Goals

To appreciate the power of language and conversations in getting work done, discuss with other like-minded participants the uncertainty of change and how it impacts Indigenous Australians.

Please note: picture of Harriet and Gordon attached as the couple.
Nice to have
• Loggo
Your ideas and creativity based on the course syllabus
An editable document so that I can insert and or change venue details whenever I deliver training in another state.

REGISTRATION DETAILS

enquiries to Harriet Dunmore 1800 947 315

COMPANY DETAILS

www.tarnlee.com.au
PO Box 836, Wyong, NSW 2259

```html
<!DOCTYPE html>
<html lang="en">
<head>
<meta charset="utf-8">
<title>Deep Mentoring for Mentors – Brochure</title>
<link rel="stylesheet" href="https://fonts.googleapis.com/css2?family=Roboto+Condensed:wght@400;700&family=Source+Sans+3:wght@400;600;700&display=swap">
<style>
  :root {
    --ink: #1f1f1f;
    --black: #000000;
    --grey-panel: #7d7d7d;
    --grey-bar: #d6d6d6;
    --gold: #c98f1c;
    --maroon: #9c2a35;
    --paper: #ffffff;
    --stage: #e9e9e9;
  }
  * { box-sizing: border-box; margin: 0; padding: 0; }
  html, body { width: 1200px; height: 960px; overflow: hidden; background: var(--stage); }
  .spread {
    position: absolute; left: 20px; top: 56px; width: 1160px; height: 848px;
    display: flex; background: var(--paper); box-shadow: 0 4px 18px rgba(0,0,0,.25);
    font-family: "Source Sans 3", Arial, sans-serif; color: var(--ink);
  }
  .panel { position: relative; width: 580px; height: 848px; overflow: hidden; }
  .panel--back { border-right: 1px solid #cfcfcf; }
  .panel-shapes { position: absolute; left: 0; top: 0; }
  .footer-band {
    position: absolute; left: 0; bottom: 0; width: 100%; height: 26px; background: var(--black);
    color: #fff; font-family: "Roboto Condensed", Arial, sans-serif; font-size: 16px;
    text-align: center; line-height: 26px;
  }
  .condensed { font-family: "Roboto Condensed", Arial, sans-serif; font-weight: 400; }

  /* back panel */
  .director-photo {
    position: absolute; left: 22px; top: 64px; width: 213px; height: 313px;
    border: 2px solid #fff; border-radius: 4px;
    background: linear-gradient(180deg, #7fa35a 0%, #5f8544 40%, #9a9a98 70%, #7a7a78 100%);
  }
  .contact { position: absolute; left: 302px; top: 318px; color: #fff; font-size: 22px; line-height: 26px; }
  .trainers { position: absolute; left: 24px; top: 388px; width: 250px; }
  .trainers-title { font-family: "Roboto Condensed", Arial, sans-serif; font-weight: 700; font-size: 15px; line-height: 18px; color: var(--maroon); }
  .trainers-text { font-size: 12.5px; line-height: 15px; }
  .section-bar {
    position: absolute; height: 27px; background: var(--grey-bar);
    font-family: "Roboto Condensed", Arial, sans-serif; font-weight: 400; font-size: 25px; line-height: 27px;
    padding-left: 11px; color: var(--ink);
  }
  .goals { position: absolute; left: 48px; top: 510px; width: 510px; list-style: none; font-size: 14.5px; line-height: 16.5px; }
  .goals li { position: relative; padding-left: 12px; margin-bottom: 7px; }
  .goals li::before { content: "•"; position: absolute; left: 0; }

  /* front panel */
  .brand { position: absolute; left: 30px; top: 104px; display: flex; align-items: center; gap: 10px; }
  .brand-name { font-family: "Roboto Condensed", Arial, sans-serif; font-weight: 700; font-size: 62px; color: var(--ink); line-height: 1; }
  .brand-dot { width: 44px; height: 44px; border-radius: 50%; background: var(--maroon); }
  .event-details { position: absolute; left: 32px; top: 186px; width: 200px; font-family: "Roboto Condensed", Arial, sans-serif; font-size: 14.5px; line-height: 18px; }
  .event-details .format { color: var(--gold); font-weight: 700; }
  .course-title { position: absolute; left: 38px; top: 282px; font-size: 29px; line-height: 30px; color: var(--ink); }
  .tag {
    position: absolute; left: 36px; width: 240px; height: 41px; border-radius: 4px;
    font-family: "Roboto Condensed", Arial, sans-serif; font-size: 27px; line-height: 41px; padding-left: 13px;
  }
  .tag--syllabus { top: 368px; background: var(--gold); color: #fff; word-spacing: 10px; }
  .tag--about { top: 423px; background: var(--black); color: var(--gold); }
  .mission { position: absolute; left: 36px; top: 512px; width: 530px; font-size: 14.5px; line-height: 16.5px; }
  .objectives-intro { position: absolute; left: 36px; top: 620px; width: 500px; color: var(--gold); font-size: 14.5px; line-height: 18px; }
  .objectives { position: absolute; left: 38px; top: 660px; width: 520px; list-style: none; font-size: 11.5px; line-height: 14px; }
  .objectives li { position: relative; padding-left: 11px; margin-bottom: 8px; }
  .objectives li::before { content: ">"; position: absolute; left: 0; }
</style>
</head>
<body>
<main class="spread">

  <section class="panel panel--back">
    <svg class="panel-shapes" width="580" height="848" viewBox="0 0 580 848" aria-hidden="true">
      <circle cx="448" cy="200" r="245" fill="var(--grey-panel)"/>
      <circle cx="90" cy="70" r="290" fill="var(--black)"/>
    </svg>
    <div class="director-photo" role="img" aria-label="Photo of directors Harriet Dunmore and Gordon Pelkin standing outdoors"></div>
    <p class="contact condensed">Call us: 61 2 4398 2716<br>Email: hello@tarnlee.com.au<br>www.tarnlee.com.au</p>

    <div class="trainers">
      <h3 class="trainers-title">Our Trainers</h3>
      <p class="trainers-text">Directors Harriet Dunmore and Gordon Pelkin lead our specialist Indigenous trainers.</p>
    </div>

    <h2 class="section-bar" style="left:38px; top:467px; width:226px;">Learning Goals</h2>
    <ul class="goals">
      <li>To appreciate the power of language and conversation in  getting work done, the quality of workplace relationships, and job satisfaction in 21st Century workplaces;</li>
      <li>Discuss the importance of living in a context that you create for your mentee;</li>
      <li>Discuss with other like-minded participants the uncertainty of continual and massive upheaval and change and how that impacts Indigenous Australians and the implications for existence</li>
      <li>Understand the key conversation and language distinctions and how to use them to good effect;</li>
      <li>How to manage your own, and the moods of others to avoid the often unintended destructive and negative impact of certain moods in work teams and workplaces;</li>
      <li>Appreciate how critically important integrity and trust are to positive working relationships and getting work done,  and practical ways as to how you can contribute to that.</li>
    </ul>
    <div class="footer-band">www.tarnlee.com.au</div>
  </section>

  <section class="panel panel--front">
    <svg class="panel-shapes" width="580" height="848" viewBox="0 0 580 848" aria-hidden="true">
      <defs>
        <linearGradient id="meetingTones" x1="0" y1="0" x2="1" y2="1">
          <stop offset="0" stop-color="#e8e6e2"/>
          <stop offset=".5" stop-color="#b9b2a8"/>
          <stop offset="1" stop-color="#ece8e1"/>
        </linearGradient>
      </defs>
      <path d="M288 374 C 320 345, 360 340, 400 350 C 470 360, 540 345, 580 322 L 580 334 C 500 378, 390 384, 288 374 Z" fill="var(--maroon)"/>
      <circle cx="425" cy="168" r="192" fill="url(#meetingTones)" role="img" aria-label="Photo of smiling professionals seated at a meeting table"/>
    </svg>

    <div class="brand">
      <span class="brand-name">TKO</span>
      <span class="brand-dot"></span>
    </div>

    <div class="event-details">
      <p class="format">Sharp two-day program</p>
      <p>Parramatta, Sydney NSW</p>
      <p>Enquiries: Harriet Dunmore</p>
      <p>1800 947 315</p>
    </div>

    <h1 class="course-title condensed">DEEP MENTORING<br>FOR MENTORS</h1>
    <div class="tag tag--syllabus">COURSE SYLLABUS</div>
    <div class="tag tag--about">ABOUT THE COURSE</div>

    <h2 class="section-bar" style="left:36px; top:474px; width:224px;">Course Mission</h2>
    <p class="mission">That as a mentor you will understand the principals of deep mentoring and how to create powerful, constructive conversationsto get what you want.</p>

    <h2 class="section-bar" style="left:36px; top:583px; width:224px;">Learning Objectives</h2>
    <p class="objectives-intro">After completing the course, you will learn powerful new distinctions that will improve your knowledge and practice base to:</p>
    <ul class="objectives">
      <li>acquire powerful distinctions in conversation and language that give you access to unlock the benefits of mentoring;</li>
      <li>develop conversation and language skills that will increase your capacity to getting your voice heard, influencing your mentee and improving the quality of your immediate working relationships</li>
      <li>learn practical problem solving and solution focused methods to address  workplace concerns with your mentee;</li>
      <li>Improve personal work effectiveness and your own productivity and</li>
      <li>Understand and manage moods in the workplace-your own and others.</li>
    </ul>
    <div class="footer-band">www.tarnlee.com.au</div>
  </section>

</main>
</body>
</html>
```